Business Cards Design for the electrical wholesaler: clean bold dynamic :)

We need a business card design that would follow our latest brand guidelines. As an electrical wholesaler we want to bring a fresh look and feel into the industry. The design should be clean bold and dynamic. It should come alive with the renewed energy of our green colour. Our grey colour should keep things balanced and complement the notion of maturity and responsibility. We employ Lato as a corporate font however are not bound by this font and we’re open to interpretation here.

Target Market(s)

Electrical contractors

Industry/Entity Type

Business

Contact Information for Business Card

Logo
Name & Surname: Olena Dovbush
Job Title: Director of Marketing
Email: helen.dovbush@mailvane.example
Cell phone: 780.555.0142
Address: 20917 - 87 Ave. Edmonton, AB, Canada. T6K 2R8
Business Phone: 780.555.0187
Website: www.qorvil.example

Font styles to use
Other font styles liked:
• Lato

Requirements
Must have
• Logo & website
Nice to have
• Brand elements - some of them you may find in the attached Brand Guidelines (e.g. three lines on the background signifying "W")

```html
<!DOCTYPE html>
<html lang="en">
<head>
<meta charset="utf-8">
<title>Qorvil business cards</title>
<link href="https://fonts.googleapis.com/css2?family=Lato:wght@400;700&display=swap" rel="stylesheet">
<style>
  :root {
    --bg: #ecebe8;
    --grey-light: #63676a;
    --grey-dark: #2f3133;
    --green: #5cb02a;
    --green-light: #9ed046;
    --accent: #e4521f;
    --text: #ffffff;
    --text-soft: #e6e8e9;
  }
  * { box-sizing: border-box; margin: 0; padding: 0; }
  html, body {
    width: 1200px; height: 800px; overflow: hidden;
    background: var(--bg);
    font-family: "Lato", sans-serif;
  }
  .sheet {
    width: 1200px; height: 800px;
    display: flex; flex-direction: column;
    align-items: center; justify-content: center; gap: 40px;
  }
  .card {
    position: relative;
    width: 560px; height: 320px;
    border-radius: 22px;
    overflow: hidden;
    background: radial-gradient(ellipse at 60% 10%, var(--grey-light) 0%, #4a4d50 45%, var(--grey-dark) 100%);
    box-shadow: 0 10px 24px rgba(0,0,0,0.25);
    color: var(--text);
  }
  /* back side */
  .card-back .brand {
    position: absolute; left: 130px; top: 92px;
    display: flex; flex-direction: column; align-items: flex-start;
  }
  .brand-row { display: flex; align-items: center; gap: 12px; }
  .brand-dot { width: 16px; height: 16px; border-radius: 50%; background: var(--green-light); }
  .brand-name { font-weight: 400; color: var(--text); letter-spacing: 1px; }
  .card-back .brand-name { font-size: 62px; line-height: 1; }
  .brand-tag {
    font-size: 10px; letter-spacing: 1.5px; text-transform: uppercase;
    color: var(--green); margin-top: 6px;
  }
  .card-back .brand-tag { margin-left: 28px; }
  .card-back .web {
    position: absolute; right: 28px; bottom: 36px;
    font-size: 14px; color: var(--text-soft); letter-spacing: 0.5px;
  }
  .band-bottom {
    position: absolute; left: 0; right: 0; bottom: 0; height: 22px;
    background: linear-gradient(90deg, var(--green) 0%, var(--green-light) 100%);
  }
  /* front side */
  .band-left {
    position: absolute; left: 0; top: 0; bottom: 0; width: 26px;
    background: linear-gradient(180deg, var(--green-light) 0%, var(--green) 100%);
  }
  .card-front .brand {
    position: absolute; right: 34px; top: 56px;
    display: flex; flex-direction: column; align-items: flex-end;
  }
  .card-front .brand-name { font-size: 40px; line-height: 1; }
  .card-front .brand-tag { font-size: 8px; }
  .person { position: absolute; left: 58px; top: 138px; }
  .person-name { font-size: 26px; font-weight: 700; letter-spacing: 0.3px; line-height: 1.2; }
  .person-title { font-size: 14px; color: var(--text-soft); margin-top: 2px; }
  .rule {
    position: absolute; left: 58px; top: 196px; width: 420px; height: 1px;
    background: linear-gradient(90deg, var(--green) 0%, rgba(92,176,42,0.5) 60%, rgba(92,176,42,0) 100%);
  }
  .contacts {
    position: absolute; left: 58px; top: 206px;
    list-style: none; font-size: 14px; line-height: 22px; color: var(--text-soft);
  }
  .contacts li { display: flex; align-items: center; gap: 10px; }
  .contacts svg { width: 13px; height: 13px; flex: none; fill: var(--accent); }
</style>
</head>
<body>
<main class="sheet">

  <section class="card card-back" aria-label="Card back">
    <div class="brand">
      <div class="brand-row">
        <span class="brand-dot"></span>
        <span class="brand-name">qorvil</span>
      </div>
      <span class="brand-tag">Electrical Wholesalers</span>
    </div>
    <span class="web">www.qorvil.example</span>
    <div class="band-bottom"></div>
  </section>

  <section class="card card-front" aria-label="Card front">
    <div class="band-left"></div>
    <div class="brand">
      <div class="brand-row">
        <span class="brand-dot"></span>
        <span class="brand-name">qorvil</span>
      </div>
      <span class="brand-tag">Electrical Wholesalers</span>
    </div>
    <div class="person">
      <h1 class="person-name">Olena Dovbush</h1>
      <p class="person-title">Director of Marketing</p>
    </div>
    <div class="rule"></div>
    <ul class="contacts">
      <li>
        <svg viewBox="0 0 24 24" aria-hidden="true"><path d="M6.6 10.8a15.1 15.1 0 0 0 6.6 6.6l2.2-2.2a1 1 0 0 1 1-.25 11.4 11.4 0 0 0 3.6.57 1 1 0 0 1 1 1V20a1 1 0 0 1-1 1A17 17 0 0 1 3 4a1 1 0 0 1 1-1h3.5a1 1 0 0 1 1 1c0 1.25.2 2.45.57 3.57a1 1 0 0 1-.25 1z"/></svg>
        780.555.0187
      </li>
      <li>
        <svg viewBox="0 0 24 24" aria-hidden="true"><path d="M7 1h10a2 2 0 0 1 2 2v18a2 2 0 0 1-2 2H7a2 2 0 0 1-2-2V3a2 2 0 0 1 2-2zm0 3v14h10V4zm5 15.5a1.2 1.2 0 1 0 0 2.4 1.2 1.2 0 0 0 0-2.4z"/></svg>
        780.555.0142
      </li>
      <li>
        <svg viewBox="0 0 24 24" aria-hidden="true"><path d="M2 5h20v14H2zm2 2v.5l8 5 8-5V7zm0 2.8V17h16V9.8l-8 5z"/></svg>
        helen.dovbush@mailvane.example
      </li>
      <li>
        <svg viewBox="0 0 24 24" aria-hidden="true"><path d="M12 2a7 7 0 0 0-7 7c0 5.2 7 13 7 13s7-7.8 7-13a7 7 0 0 0-7-7zm0 9.5A2.5 2.5 0 1 1 12 6.5a2.5 2.5 0 0 1 0 5z"/></svg>
        20917 - 87 Ave. Edmonton, AB, Canada. T6K 2R8
      </li>
    </ul>
  </section>

</main>
</body>
</html>
```